Beautiful, impactful, engaging packaging for a box of a new granola brand

BL4Z™Muesli is a new brand – the packaging is one of the first touchpoints with consumers. Initially this will be in Farm Shops and Garden Centres; places where shoppers are looking for interesting new products and inspiration. We need to stand out in these busy, ‘homespun’ environments with an impactful, distinctive and engaging pack design.

The key brand communication objectives are:
o The create a unique and own-able pack design that builds a powerful Bl4z™Muesli brand
o To reflect FRESH with an ambient product in an ambient category
o To communicate our mission to create ‘an irresistible breakfast that brings families together at the breakfast table’; our passion for food and our strong natural foodie values
o To use the pack as a start point for an on-going dialogue with consumers – one that we hope will continue through social media channels (as there will be little other marketing support)

On a practical level we also need to:
o Visually disrupt the fixture providing stand-out and strong shelf blocking using the 3 variants
o Have a pack design that will work as well in Farms Shops as in mainstream grocers so that it remains constant as we develop and grow across the retail trade

Carton dimensions - height 240mm x width 160mm x depth 50mm

Target Market(s)

• 35-55-year-old busy women – pinpoint 40yrs mums
• Enjoy cooking and ideally want to make from scratch, but lack time and inspiration
• Health aware, look after themselves and choose ‘better for you’ options as a balance to their indulgences
• Like to try new things, quite experimental, especially when it comes to food. Actively seek out new food at Farmers Markets and Food Shows
• Have more time at the weekend, especially for breakfast, and want quick, convenient, healthy, delicious options to start the day
• Love spending time together as a family, really appreciate moments when everyone comes together
• Take pride in serving up delicious food; love getting positive feedback
• Delighted to find a short cut (especially undetected) and shares discoveries with friends
• Currently buy meal kits for quick evening meals and may even buy ‘Crate Chef’ or ‘Plattio’
• More likely to shop for groceries on Vendly or at Marlowes or Pennocks (or even Bovk). Likes to pop a few culinary treats into the basket.

Industry/Entity Type

Farm

Font styles to use
Sans Serif
Decorative

Requirements
Must have
• We see Bl4z™Muesli as a warm, stylish, modern, authentic brand that connects with the consumer in an emotional way. They should really feel it is a brand that speaks to them personally, one that they are proud to buy.
• Must haves:
• * BlazMuesli logo
• * 'stay blaz with us' strapline
• * 'Toasting Kit' descriptor on the front and 'Fresh Granola Toasting Kit' on the back
• * 3 step process communicated - 1. Mix 2.Toast 3. Eat
• * Show that it contains all natural ingredients - nuts, seeds, oats and honey
• * 3 colourways - one for each of the 3 variants (Mega Berrylicious, Mega Crunchy and Mega Grainy)
• * Freshness / natural cues
• *Communicate - "No artificial colours, flavours or preservatives; good source of fibre, source of protein; no refined sugar"
Nice to have
• * Should it have a picture of a bowl of granola on the front? Not sure...
• * Is there an opportunity for the design to link across the variants to create more visual impact at point of sale
Should not have
• * not too fussy or complicated - we prefer simple, bold elegance

```html
<!DOCTYPE html>
<html lang="en">
<head>
<meta charset="utf-8">
<title>BlazMuesli Toasting Kit – Three Variants</title>
<link rel="stylesheet" href="https://fonts.googleapis.com/css2?family=Arvo:wght@700&family=Fredoka:wght@500;600&family=Kalam:wght@700&family=Oswald:wght@400;500&family=Roboto:wght@400;500&family=Roboto+Slab:wght@700&display=swap">
<style>
  :root {
    --canvas: #ffffff;
    --brand-teal: #2e9aa0;
    --leaf-green: #6e9a3a;
    --pill-green: #7a9a48;
    --pill-green-light: #9cb96a;
    --headline-green: #1f6b3a;
    --ink: #1e1e1e;
    --photo-warm: #c89a5a;
    --photo-deep: #8a5a2c;
    --bowl-white: #f4f4f2;
    --ribbon-green: #739a45;
    --ribbon-yellow: #f2c230;
    --honey: #f0a020;
  }
  * { margin: 0; padding: 0; box-sizing: border-box; }
  html, body { width: 1200px; height: 1200px; overflow: hidden; background: var(--canvas); }
  .canvas { position: relative; width: 1200px; height: 1200px; }

  .pack {
    position: absolute; top: 246px; width: 368px; height: 556px;
    background: var(--pack-bg); overflow: hidden;
  }
  .pack--nutty  { left: 20px;  --pack-bg: #f0ede5; --band: #8a5a3b; --step1: #c39a72; --step2: #5a3516; --step3: #3aa843; --variant: #4a3520; }
  .pack--seedy  { left: 422px; --pack-bg: #e4f0da; --band: #8cc63f; --step1: #c6b9a6; --step2: #8cc63f; --step3: #f6a83a; --variant: #e8413a; }
  .pack--fruity { left: 816px; --pack-bg: #fde8cd; --band: #c8202e; --step1: #e8222e; --step2: #ec5a2a; --step3: #3aa843; --variant: #c2203a; }

  .claims-band {
    height: 37px; background: var(--band); color: #fff;
    font: 400 13px/37px "Oswald", sans-serif; letter-spacing: -0.2px;
    padding-left: 7px; white-space: nowrap;
  }

  .brand {
    position: absolute; top: 72px; left: 0; width: 100%; text-align: center;
  }
  .brand__name {
    display: inline-flex; align-items: center; gap: 5px;
    font: 600 21px/1 "Fredoka", sans-serif; color: var(--brand-teal);
  }
  .brand__dot { width: 9px; height: 9px; border-radius: 50%; background: var(--leaf-green); }
  .brand__strap { font: 400 7px/1 "Roboto", sans-serif; color: var(--brand-teal); margin-top: 3px; }

  .fresh-pill {
    position: absolute; left: 88px; top: 133px; width: 204px; height: 42px;
    border-radius: 12px; border: 3px solid #fff;
    background: linear-gradient(90deg, var(--pill-green) 0%, var(--pill-green-light) 50%, var(--pill-green) 100%);
    color: #fff; text-align: center; font: 700 40px/36px "Roboto Slab", serif;
  }
  .descriptor {
    position: absolute; top: 176px; left: 0; width: 100%; text-align: center;
    font: 700 29px/1.2 "Kalam", cursive; color: var(--ink);
  }

  .steps { position: absolute; top: 212px; left: 0; width: 100%; height: 62px; }
  .step {
    position: absolute; top: 0; width: 62px; height: 62px; border-radius: 50%;
    color: #fff; text-align: center; font-family: "Roboto", sans-serif; font-weight: 500;
  }
  .step span { display: block; }
  .step__num { font-size: 16px; line-height: 1; padding-top: 11px; }
  .step__word { font-size: 22px; line-height: 0.95; letter-spacing: -0.5px; }
  .step--mix   { left: 101px; background: var(--step1); }
  .step--toast { left: 155px; background: var(--step2); }
  .step--eat   { left: 212px; background: var(--step3); }

  .product-photo {
    position: absolute; left: 0; top: 300px; width: 368px; height: 256px;
    background:
      radial-gradient(ellipse 62% 58% at 55% 70%, var(--photo-warm) 0%, var(--photo-deep) 55%, transparent 72%),
      radial-gradient(ellipse 95% 85% at 55% 72%, var(--bowl-white) 0%, #dcdcd8 70%, var(--pack-bg) 100%);
  }

  .headline { position: absolute; top: 270px; left: 0; width: 100%; text-align: center; }
  .headline__lead { font: 600 44px/1 "Fredoka", sans-serif; color: var(--headline-green); letter-spacing: -0.5px; }
  .headline__variant { font: 700 44px/1 "Arvo", serif; color: var(--variant); margin-top: -4px; }

  .ingredients { position: absolute; left: 0; top: 416px; width: 190px; height: 132px; }
  .ingredients svg { position: absolute; inset: 0; }
  .ingredients__text {
    position: absolute; left: 8px; top: 12px; transform: rotate(-4deg); transform-origin: left top;
    color: #fff;
  }
  .ingredients__title { font: 700 19px/0.95 "Roboto Slab", serif; letter-spacing: -0.5px; }
  .ingredients__list { list-style: none; margin-left: 30px; margin-top: 2px; }
  .ingredients__list li {
    font: 500 12px/15px "Roboto", sans-serif; border-bottom: 1px solid rgba(255,255,255,.7); width: 90px; padding-left: 8px;
  }
  .ingredients__list .is-nuts { font-weight: 700; font-size: 13px; }
  .ingredients__list .is-seeds { font-family: "Roboto Slab", serif; color: #e6eed8; }
  .ingredients__list .is-honey { font: 700 13px/15px "Kalam", cursive; color: var(--honey); border: 0; }
</style>
</head>
<body>
<main class="canvas">

  <section class="pack pack--nutty">
    <div class="claims-band">NO artificial colours flavours I NO preservatives &nbsp;I NO refined sugar</div>
    <div class="product-photo" role="img" aria-label="Photo of a white bowl of toasted granola with nuts and dried berries"></div>
    <div class="brand">
      <div class="brand__name"><span class="brand__dot"></span>BlazMuesli</div>
      <div class="brand__strap">stay blaz with us</div>
    </div>
    <div class="fresh-pill">FRESH</div>
    <div class="descriptor">Granola Toasting Kit</div>
    <div class="steps">
      <div class="step step--mix"><span class="step__num">1</span><span class="step__word">mix</span></div>
      <div class="step step--toast"><span class="step__num">2</span><span class="step__word">toast</span></div>
      <div class="step step--eat"><span class="step__num">3</span><span class="step__word">eat</span></div>
    </div>
    <div class="headline">
      <div class="headline__lead">Wonderfully</div>
      <div class="headline__variant">NUTTY</div>
    </div>
    <div class="ingredients">
      <svg viewBox="0 0 190 132" aria-hidden="true">
        <polygon points="0,12 160,2 190,0 168,104 0,124" fill="var(--ribbon-green)"/>
        <polygon points="0,124 168,104 166,112 0,132" fill="var(--ribbon-yellow)"/>
      </svg>
      <div class="ingredients__text">
        <div class="ingredients__title">ALL NATURAL<br>INGREDIENTS</div>
        <ul class="ingredients__list">
          <li class="is-nuts">NUTS</li><li class="is-seeds">SEEDS</li><li>OATS</li><li class="is-honey">Honey</li>
        </ul>
      </div>
    </div>
  </section>

  <section class="pack pack--seedy">
    <div class="claims-band">NO artificial colours flavours I NO preservatives &nbsp;I NO refined sugar</div>
    <div class="product-photo" role="img" aria-label="Photo of a white bowl of toasted granola with seeds and dried berries"></div>
    <div class="brand">
      <div class="brand__name"><span class="brand__dot"></span>BlazMuesli</div>
      <div class="brand__strap">stay blaz with us</div>
    </div>
    <div class="fresh-pill">FRESH</div>
    <div class="descriptor">Granola Toasting Kit</div>
    <div class="steps">
      <div class="step step--mix"><span class="step__num">1</span><span class="step__word">mix</span></div>
      <div class="step step--toast"><span class="step__num">2</span><span class="step__word">toast</span></div>
      <div class="step step--eat"><span class="step__num">3</span><span class="step__word">eat</span></div>
    </div>
    <div class="headline">
      <div class="headline__lead">Wonderfully</div>
      <div class="headline__variant">SEEDY</div>
    </div>
    <div class="ingredients">
      <svg viewBox="0 0 190 132" aria-hidden="true">
        <polygon points="0,12 160,2 190,0 168,104 0,124" fill="var(--ribbon-green)"/>
        <polygon points="0,124 168,104 166,112 0,132" fill="var(--ribbon-yellow)"/>
      </svg>
      <div class="ingredients__text">
        <div class="ingredients__title">ALL NATURAL<br>INGREDIENTS</div>
        <ul class="ingredients__list">
          <li class="is-nuts">NUTS</li><li class="is-seeds">SEEDS</li><li>OATS</li><li class="is-honey">Honey</li>
        </ul>
      </div>
    </div>
  </section>

  <section class="pack pack--fruity">
    <div class="claims-band">NO artificial colours flavours I NO preservatives &nbsp;I NO refined sugar</div>
    <div class="product-photo" role="img" aria-label="Photo of a white bowl of toasted granola with dried fruit"></div>
    <div class="brand">
      <div class="brand__name"><span class="brand__dot"></span>BlazMuesli</div>
      <div class="brand__strap">stay blaz with us</div>
    </div>
    <div class="fresh-pill">FRESH</div>
    <div class="descriptor">Granola Toasting Kit</div>
    <div class="steps">
      <div class="step step--mix"><span class="step__num">1</span><span class="step__word">mix</span></div>
      <div class="step step--toast"><span class="step__num">2</span><span class="step__word">toast</span></div>
      <div class="step step--eat"><span class="step__num">3</span><span class="step__word">eat</span></div>
    </div>
    <div class="headline">
      <div class="headline__lead">Wonderfully</div>
      <div class="headline__variant">FRUITY</div>
    </div>
    <div class="ingredients">
      <svg viewBox="0 0 190 132" aria-hidden="true">
        <polygon points="0,12 160,2 190,0 168,104 0,124" fill="var(--ribbon-green)"/>
        <polygon points="0,124 168,104 166,112 0,132" fill="var(--ribbon-yellow)"/>
      </svg>
      <div class="ingredients__text">
        <div class="ingredients__title">ALL NATURAL<br>INGREDIENTS</div>
        <ul class="ingredients__list">
          <li class="is-nuts">NUTS</li><li class="is-seeds">SEEDS</li><li>OATS</li><li class="is-honey">Honey</li>
        </ul>
      </div>
    </div>
  </section>

</main>
</body>
</html>
```